Menu for Traditional Persian Restraunt with Hookah - Name of Restaraunt is Venaro

We are a traditional Persian Restaraunt. We Provide Home Made Fresh Tradition Persian Meals Here in Sydney Australia
We also offer a Shisha Service in our back section of our Restaraunt.
The Restaurant Layout is like it is in IRAN, Very Unique nothing like it here in Australia. Day beds, persian Carpet, Timber Walls, Copper Lighting, Just to name a few. We want a menu that stands out and is very traditional in the Persian Way, but also is understandable for someone that isnt persian. Our Logo is a Sky Blue Colour ( which is a traditional well known colour in our country) Everything is Freshly made . We are open 7 days. Will Add Food Details andc Images in the next coming Days

Attached is our logo. I would want a space if possible to have an image of each food next to the decription. You can give me multiple option with or without, but some sort of images should be displayed even the footer and header of the menu.

I will be getting the menu printed as an A4 style book with leather front and back hard cover

I would like a SPEcial of the day Setion at the end of the menu with an emty page so i can put items on there.

Please give me ideas as i will be changing the items on special every few days

One of competitors is The Golden Ewer, Also if you have a quick look on google and type Tradition persian Food you will get an idea of the food and type of culture it is

Target Market(s)

All Cultures< Especially persians

Industry/Entity Type

It Service

Font styles to use
Sans Serif

Requirements
Must have
• Must have Blue colour Logo Provided
• Menu for Food
• Menu for Hookah
• Menu for Coffee
• Seperate Menu for Takeaway
Nice to have
• Traditional type theme in background like persian carpet( google search - hand made traditional carpet)
• needs to be easily read and undestandable

```html
<!DOCTYPE html>
<html lang="en">
<head>
<meta charset="utf-8">
<title>Venaro — Special</title>
<link href="https://fonts.googleapis.com/css2?family=Cinzel:wght@600&family=Jost:wght@400;600&display=swap" rel="stylesheet">
<style>
  :root {
    --sky: #2fd0ee;
    --ink: #111111;
    --navy: #1d2a4a;
    --paper: #ffffff;
    --text: #2a2a2a;
    --tick: #d4161c;
    --ornament-light: #f4f4f4;
    --ornament-mid: #d9d9d9;
  }
  * { margin: 0; padding: 0; box-sizing: border-box; }
  html, body { width: 855px; height: 1200px; overflow: hidden; background: var(--paper); }
  .menu-page {
    position: relative;
    width: 855px;
    height: 1200px;
    background: var(--paper);
    overflow: hidden;
    font-family: "Jost", Arial, sans-serif;
    color: var(--text);
  }
  .header-band {
    position: absolute;
    left: 0; top: 0;
    width: 855px; height: 157px;
    background: var(--sky);
  }
  .page-title {
    position: absolute;
    left: 48px; top: 40px;
    font-family: "Cinzel", Georgia, serif;
    font-weight: 600;
    font-size: 112px;
    line-height: 1;
    color: var(--paper);
    letter-spacing: 2px;
  }
  .brand-name {
    position: absolute;
    right: 26px; top: 22px;
    font-family: "Jost", Arial, sans-serif;
    font-weight: 600;
    font-size: 22px;
    color: var(--navy);
    letter-spacing: 1px;
  }
  .side-strip {
    position: absolute;
    left: 0; top: 157px;
    width: 157px; height: 1043px;
    background: var(--ink);
  }
  .ornament-field {
    position: absolute;
    left: 157px; top: 700px;
    width: 698px; height: 500px;
    background: radial-gradient(ellipse at 40% 55%, var(--ornament-light) 0%, var(--paper) 45%, var(--ornament-mid) 100%);
  }
  .special-list { list-style: none; }
  .special-item {
    position: absolute;
    left: 271px;
    width: 455px;
  }
  .dish-name {
    font-weight: 600;
    font-size: 16px;
    color: var(--ink);
    line-height: 1.3;
  }
  .dish-desc {
    font-weight: 400;
    font-size: 13.5px;
    line-height: 1.35;
    color: var(--text);
  }
  .choice-circle {
    position: absolute;
    left: 752px;
    width: 28px; height: 28px;
    border: 2px solid var(--ink);
    border-radius: 50%;
  }
  .tick-mark {
    position: absolute;
    left: 748px; top: 292px;
  }
</style>
</head>
<body>
<main class="menu-page">
  <header class="header-band">
    <h1 class="page-title">SPECIAL</h1>
    <div class="brand-name">Venaro</div>
  </header>

  <div class="side-strip"></div>
  <div class="ornament-field" role="img" aria-label="Decorative Persian floral line pattern in black and white"></div>

  <ul class="special-list">
    <li class="special-item" style="top:226px">
      <div class="dish-name">Lamb Shank Mahichae &nbsp;$ 9.00</div>
      <div class="dish-desc">Lamb dish served with rice</div>
    </li>
    <li class="special-item" style="top:288px">
      <div class="dish-name">Khoreshte Geymeh &nbsp;$ 6.90</div>
      <div class="dish-desc">Yellow split peas cooked with ripe tomatoes, dried lime, lamb pieces, garnished with fried potatoes &amp; served with rice</div>
    </li>
    <li class="special-item" style="top:410px">
      <div class="dish-name">Khoreshte Bamieh &nbsp;$ 6.90</div>
      <div class="dish-desc">Lamb pieces with okra cooked in tomato sauce &amp; garlic, served with rice</div>
    </li>
    <li class="special-item" style="top:512px">
      <div class="dish-name">Khoreshte Ghormeh Sabzi &nbsp;$ 6.90</div>
      <div class="dish-desc">Fried chopped parsley, coriander &amp; leeks cooked with sun-dried lime, pieces of lamb &amp; kidney beans, served with rice</div>
    </li>
    <li class="special-item" style="top:636px">
      <div class="dish-name">Zereshk Pollo &nbsp;$ 8.00</div>
      <div class="dish-desc">Quarter chicken, served with basmati rice mixed with barberries &amp; saffron</div>
    </li>
  </ul>

  <span class="choice-circle" style="top:218px"></span>
  <span class="choice-circle" style="top:302px"></span>
  <span class="choice-circle" style="top:418px"></span>
  <span class="choice-circle" style="top:520px"></span>
  <span class="choice-circle" style="top:644px"></span>

  <svg class="tick-mark" width="80" height="60" viewBox="0 0 80 60" aria-hidden="true">
    <path d="M6 30 L24 48 L76 6" fill="none" stroke="var(--tick)" stroke-width="7" stroke-linecap="round" stroke-linejoin="round"/>
  </svg>
</main>
</body>
</html>
```